New Business Card Design Project

We require a business card design for Pharvelix, a newly established Indian company.
Our focus is on the development, manufacturing, and export of a diverse array of pharmaceutical products on a global scale. The card should convey a professional appearance, as our primary markets are in Africa, China, and Southeast Asian nations.
We envision a two-sided business card, with the reverse side dedicated to a logo set against a solid color or an elegantly designed pattern. The corners should be rounded. We would appreciate seeing both horizontal and vertical design options. We trust the designer to utilize their expertise in creating this design.

The content for the business card is included in the attached Word file.

Target Market(s)

Our primary markets are in Africa, China, and Southeast Asian, Latin America, Maldives, Sri Lanka

Industry/Entity Type

Pharmaceutical Manufacturing and Export

Contact Information for Business Card

Colors

Designer to choose colors to be used in the design.

Requirements
Must have
• The reverse side of the business card features solely the logo along with the tagline, "Remedies of Life."
Should not have
• The logo should not exceed two instances, encompassing both the front and back sides of the card.

```html
<!DOCTYPE html>
<html lang="en">
<head>
<meta charset="utf-8">
<title>Pharvelix Business Card</title>
<link rel="stylesheet" href="https://fonts.googleapis.com/css2?family=Poppins:wght@700&family=Arimo:wght@400&display=swap">
<style>
  :root {
    --stage: #151418;
    --card-light: #ffffff;
    --card-dark: #1c1b20;
    --brand-blue: #25a6e0;
    --brand-red: #ef5a45;
    --ink-grey: #6b6b70;
    --rule-grey: #8a8a90;
    --emboss: #37363d;
  }
  * { margin: 0; padding: 0; box-sizing: border-box; }
  html, body { width: 1200px; height: 963px; overflow: hidden; }
  body {
    background: var(--stage);
    display: flex;
    flex-direction: column;
    align-items: center;
    justify-content: center;
    gap: 60px;
  }
  .card {
    position: relative;
    width: 600px;
    height: 343px;
    border-radius: 26px;
    border-bottom: 4px solid var(--brand-blue);
    overflow: hidden;
  }
  .card--front { background: var(--card-light); }
  .card--back {
    background: var(--card-dark);
    display: flex;
    align-items: center;
    justify-content: center;
  }
  .brand {
    display: flex;
    align-items: center;
    gap: 14px;
    font-family: "Poppins", sans-serif;
    font-weight: 700;
    letter-spacing: -0.5px;
  }
  .brand__dot { border-radius: 50%; flex: none; }
  .card--front .brand {
    position: absolute;
    left: 200px;
    top: 82px;
    color: var(--brand-blue);
    font-size: 50px;
  }
  .card--front .brand__dot { width: 26px; height: 26px; background: var(--brand-red); }
  .card--back .brand { color: var(--emboss); font-size: 64px; }
  .card--back .brand__dot { width: 34px; height: 34px; background: var(--brand-red); }

  .person {
    position: absolute;
    right: 340px;
    top: 186px;
    text-align: right;
  }
  .person__name {
    font-family: "Poppins", sans-serif;
    font-weight: 700;
    font-size: 22px;
    color: var(--brand-blue);
    white-space: nowrap;
  }
  .person__role {
    font-family: "Arimo", sans-serif;
    font-size: 17px;
    color: var(--ink-grey);
    margin-top: -2px;
  }
  .divider {
    position: absolute;
    left: 278px;
    top: 186px;
    width: 1px;
    height: 74px;
    background: var(--rule-grey);
  }
  .contact {
    position: absolute;
    left: 296px;
    top: 188px;
    list-style: none;
    font-family: "Arimo", sans-serif;
    font-size: 16px;
    color: var(--ink-grey);
  }
  .contact li { display: flex; align-items: center; gap: 8px; height: 24px; }
  .contact svg { width: 15px; height: 15px; flex: none; }
  .contact .accent { color: var(--brand-blue); }
  .address {
    position: absolute;
    left: 60px;
    top: 286px;
    font-family: "Arimo", sans-serif;
    font-size: 16px;
    color: var(--ink-grey);
  }
</style>
</head>
<body>
  <section class="card card--front" aria-label="Card front">
    <div class="brand"><span class="brand__name">Pharvelix</span><span class="brand__dot"></span></div>
    <div class="person">
      <p class="person__name">Arjun K. Mehta</p>
      <p class="person__role">CEO</p>
    </div>
    <div class="divider"></div>
    <ul class="contact">
      <li>
        <svg viewBox="0 0 16 16" aria-hidden="true"><path d="M4 1.5 6 4.5 4.6 6a8 8 0 0 0 5.4 5.4L11.5 10l3 2-1.2 2.3C7.5 14.5 1.5 8.5 1.7 2.7Z" fill="none" stroke="#25a6e0" stroke-width="1.4" stroke-linejoin="round"/></svg>
        <span>+919800012345</span>
      </li>
      <li>
        <svg viewBox="0 0 16 16" aria-hidden="true"><rect x="1.5" y="3.5" width="13" height="9" rx="1" fill="none" stroke="#25a6e0" stroke-width="1.4"/><path d="M1.5 4 8 9l6.5-5" fill="none" stroke="#25a6e0" stroke-width="1.4"/></svg>
        <span>amehta@pharvelix.com</span>
      </li>
      <li>
        <svg viewBox="0 0 16 16" aria-hidden="true"><g fill="none" stroke="#25a6e0" stroke-width="1.3"><circle cx="8" cy="8" r="6.5"/><ellipse cx="8" cy="8" rx="2.8" ry="6.5"/><path d="M1.5 8h13M2.5 4.8h11M2.5 11.2h11"/></g></svg>
        <span>www.<span class="accent">pharvelix</span>.com</span>
      </li>
    </ul>
    <p class="address">12, Lotus Nagar, Nashik, 422001, India</p>
  </section>

  <section class="card card--back" aria-label="Card back">
    <div class="brand"><span class="brand__name">Pharvelix</span><span class="brand__dot"></span></div>
  </section>
</body>
</html>
```